Book Cover "Venice"

Creation of a cover (14 x 20.5 cm + bleed area) for a book:
Image: “BrumeVerte” (Tiff joined)
AUTHOR: Corinne Valmer
TITLE: The murmurs of Lorient
PUBLISHER: Editions Pluvane (AT THE BOTTOM OF THE COVER)

Target Market(s)

Readers of romantic novels

Industry/Entity Type

Book

```html
<!DOCTYPE html>
<html lang="en">
<head>
<meta charset="utf-8">
<title>The Murmurs of Lorient — Cover Proof</title>
<link rel="stylesheet" href="https://fonts.googleapis.com/css2?family=Cormorant+Garamond:wght@500&family=Great+Vibes&family=Lato:wght@400&display=swap">
<style>
  :root {
    --paper: #f1f1f1;
    --mark: #3a3a3a;
    --sky-top: #8e1a3a;
    --sky-mid: #e0243f;
    --sky-low: #c81f3c;
    --night: #0a0406;
    --trim: #e00d1f;
    --ink: #ffffff;
  }
  * { margin: 0; padding: 0; box-sizing: border-box; }
  html, body { width: 979px; height: 1200px; overflow: hidden; background: var(--paper); }
  .proof { position: relative; width: 979px; height: 1200px; }
  .crop-marks { position: absolute; inset: 0; }
  .cover {
    position: absolute; left: 176px; top: 146px; width: 627px; height: 908px;
    overflow: hidden;
  }
  .cover-art {
    position: absolute; inset: 0;
    background:
      radial-gradient(ellipse at 50% 40%, var(--sky-mid) 0%, transparent 65%),
      linear-gradient(180deg, var(--sky-top) 0%, var(--sky-low) 30%, var(--sky-mid) 55%, #7a1024 74%, var(--night) 84%, var(--night) 100%);
  }
  .cover-lines { position: absolute; inset: 0; }
  .author {
    position: absolute; top: 34px; left: 0; width: 100%;
    text-align: center; font-family: "Lato", sans-serif; font-size: 22px;
    letter-spacing: 5px; color: var(--ink); line-height: 22px;
    padding-left: 10px;
  }
  .book-title { position: absolute; inset: 0; font-weight: normal; }
  .title { position: absolute; left: 0; width: 100%; color: var(--ink); text-align: center; display: block; white-space: nowrap; }
  .title-main {
    top: 157px; font-family: "Cormorant Garamond", serif; font-weight: 500;
    font-size: 70px; line-height: 1; letter-spacing: 0; padding-left: 16px;
  }
  .title-link {
    top: 248px; font-family: "Cormorant Garamond", serif; font-weight: 500;
    font-size: 70px; line-height: 1; padding-left: 20px;
  }
  .title-place {
    top: 262px; font-family: "Great Vibes", cursive; font-weight: 400;
    font-size: 150px; line-height: 1; padding-right: 20px;
  }
  .publisher {
    position: absolute; top: 852px; left: 0; width: 100%; text-align: center;
    font-family: "Lato", sans-serif; font-size: 17px; line-height: 22px;
    letter-spacing: 3px; color: var(--ink);
  }
</style>
</head>
<body>
<div class="proof">
  <svg class="crop-marks" width="979" height="1200" viewBox="0 0 979 1200">
    <g stroke="var(--mark)" stroke-width="0.8">
      <line x1="186.5" y1="74" x2="186.5" y2="129"/>
      <line x1="793.5" y1="74" x2="793.5" y2="129"/>
      <line x1="186.5" y1="1072" x2="186.5" y2="1126"/>
      <line x1="793.5" y1="1072" x2="793.5" y2="1126"/>
      <line x1="104" y1="156.5" x2="159" y2="156.5"/>
      <line x1="820" y1="156.5" x2="875" y2="156.5"/>
      <line x1="104" y1="1043.5" x2="159" y2="1043.5"/>
      <line x1="820" y1="1043.5" x2="875" y2="1043.5"/>
    </g>
  </svg>

  <section class="cover">
    <div class="cover-art" role="img" aria-label="Photograph: domes and bell towers in silhouette against a deep crimson sunset sky, with glowing street lanterns in the foreground"></div>

    <svg class="cover-lines" width="627" height="908" viewBox="0 0 627 908">
      <rect x="10.5" y="10.5" width="606" height="887" fill="none" stroke="var(--trim)" stroke-width="0.7"/>
      <polyline points="145,44 35,44 35,714" fill="none" stroke="var(--ink)" stroke-width="2.4"/>
      <polyline points="476,44 592,44 592,675" fill="none" stroke="var(--ink)" stroke-width="2.4"/>
    </svg>

    <p class="author">CORINNE VALMER</p>
    <h1 class="book-title">
      <span class="title title-main">THE MURMURS</span>
      <span class="title title-link">OF</span>
      <span class="title title-place">Lorient</span>
    </h1>
    <p class="publisher">Editions Pluvane</p>
  </section>
</div>
</body>
</html>
```